New startup requiring business card

New company needed a business card / logo. Company name is
Tessiv
Company is providing IT software sales, partnering and consulting services across the APAC region. Catch line is "thriving as one".
We currently have a feeling yellow as the primary colour given its meaning across the region but open to ideas. Main brief is we want something smart, clean and professional while still leveraging the strength of the name.
A major part of the business is mutually beneficial partnerships, not sure if this helps but maybe visual around linkages between objects.
Also wanting a standard size card, preference is something that will have a D/S cello sheen finish in a matt. But again open to ideas, wow us!
Software

```html
<!DOCTYPE html>
<html lang="en">
<head>
<meta charset="utf-8">
<title>Tessiv business card</title>
<link href="https://fonts.googleapis.com/css2?family=Questrial&family=Montserrat:wght@700&display=swap" rel="stylesheet">
<style>
  :root {
    --yellow: #ebe20a;
    --yellow-deep: #d9d000;
    --paper: #f7f7f7;
    --ink: #2b2b2b;
    --ink-soft: #4a4a4a;
    --backdrop: #e4e4e2;
    --white: #ffffff;
  }
  * { margin: 0; padding: 0; box-sizing: border-box; }
  html, body { width: 1200px; height: 941px; overflow: hidden; }
  body {
    background: var(--backdrop);
    font-family: "Questrial", "Helvetica Neue", Arial, sans-serif;
    position: relative;
  }
  .card {
    position: absolute;
    left: 300px;
    width: 600px;
    height: 343px;
    border-radius: 3px;
    box-shadow: 0 6px 18px rgba(0,0,0,.15);
    overflow: hidden;
  }
  .card--front { top: 88px; background: var(--paper); }
  .card--back { top: 510px; background: var(--yellow); }

  .front__band {
    position: absolute; left: 0; right: 0; bottom: 0;
    height: 12px; background: var(--yellow);
  }
  .brand { position: absolute; display: inline-block; }
  .brand__name {
    font-size: 88px; line-height: 1; letter-spacing: 1px; white-space: nowrap;
  }
  .brand__tagline {
    font-size: 15px; letter-spacing: .5px; margin-top: 4px; text-align: right; white-space: nowrap;
  }
  .card--front .brand { left: 44px; top: 44px; }
  .card--front .brand__name { color: var(--yellow); }
  .card--front .brand__tagline { color: var(--ink-soft); }

  .person { position: absolute; left: 48px; top: 210px; }
  .person__name {
    font-family: "Montserrat", Arial, sans-serif; font-weight: 700;
    font-size: 15px; color: var(--ink);
  }
  .person__role { font-size: 14px; color: var(--yellow-deep); margin-top: 2px; }
  .person__address { font-size: 14px; color: var(--ink-soft); margin-top: 16px; line-height: 1.45; }

  .contacts {
    position: absolute; right: 40px; top: 60px;
    list-style: none; font-size: 14px; color: var(--ink-soft);
  }
  .contacts li { display: flex; align-items: center; gap: 10px; height: 24px; white-space: nowrap; }
  .contacts svg { width: 12px; height: 12px; fill: var(--yellow-deep); flex: none; }

  .card--back .brand { right: 60px; bottom: 64px; }
  .card--back .brand__name { color: var(--white); font-size: 96px; }
  .card--back .brand__tagline { color: var(--white); font-size: 16px; }
</style>
</head>
<body>
  <section class="card card--front">
    <div class="brand">
      <div class="brand__name">Tessiv</div>
      <div class="brand__tagline">thriving as one</div>
    </div>

    <ul class="contacts">
      <li><svg viewBox="0 0 12 12"><path d="M2.5 1h2l1 3-1.3 1a6 6 0 0 0 2.8 2.8l1-1.3 3 1v2c0 .6-.4 1-1 1A10 10 0 0 1 1.5 2c0-.6.4-1 1-1z"/></svg>+44 (0)207 555 0142</li>
      <li><svg viewBox="0 0 12 12"><rect x="3" y="0.5" width="6" height="11" rx="1.2"/></svg>+44 (0)7700 900 318</li>
      <li><svg viewBox="0 0 12 12"><path d="M0.5 2.5h11v7h-11z"/></svg>maren.holt@tessiv.co.uk</li>
      <li><svg viewBox="0 0 12 12"><circle cx="6" cy="6" r="5.5"/></svg>www.tessiv.co.uk</li>
    </ul>

    <div class="person">
      <div class="person__name">Maren Holt</div>
      <div class="person__role">Operations Manager</div>
      <div class="person__address">14 Orchard Row Fulbridge<br>London E9 4TQ</div>
    </div>

    <div class="front__band"></div>
  </section>

  <section class="card card--back">
    <div class="brand">
      <div class="brand__name">Tessiv</div>
      <div class="brand__tagline">thriving as one</div>
    </div>
  </section>
</body>
</html>
```